TOTR 'Lower Third' for documentary TV series

Create a lower third for the series Roamers of the Ridge (airs 2019) - we are in nature for the entire series, they use birch bark canoes to travel, they eat what they can find/catch including fish and beaver, no modern technology, must be able to have name and below where they are from. thanks

Target Market(s)

TV Series

Industry/Entity Type

Tv

Colors

Designer to choose colors to be used in the design.

Requirements
Must have
• pops from screen, keep in mind we have lots of lakes, sky and forest
Nice to have
• stands out
Should not have
• i'm open

```html
<!DOCTYPE html>
<html lang="en">
<head>
<meta charset="utf-8">
<title>Roamers of the Ridge – Lower Third</title>
<link rel="stylesheet" href="https://fonts.googleapis.com/css2?family=Staatliches&display=swap">
<style>
  :root {
    --banner-yellow: #e6c033;
    --banner-yellow-light: #edcb45;
    --banner-yellow-deep: #c9a227;
    --banner-grass: #9c8a2a;
    --ink: #1d1a15;
    --scene-water: #3f5560;
    --scene-reed: #6b6a2c;
    --scene-rock: #4a463f;
    --scene-canoe: #a0512a;
  }
  * { margin: 0; padding: 0; box-sizing: border-box; }
  html, body {
    width: 1200px;
    height: 675px;
    overflow: hidden;
    background: #111;
  }
  .lower-third {
    position: relative;
    width: 1200px;
    height: 675px;
    overflow: hidden;
  }
  .scene-photo {
    position: absolute;
    inset: 0;
    background:
      radial-gradient(ellipse 40% 35% at 72% 55%, var(--scene-canoe) 0%, rgba(160,81,42,0) 70%),
      radial-gradient(ellipse 30% 30% at 30% 60%, #2a2723 0%, rgba(42,39,35,0) 70%),
      linear-gradient(100deg, var(--scene-rock) 0%, #5a564d 25%, var(--scene-reed) 55%, var(--scene-water) 80%, #2f3f47 100%);
  }

  /* worn, weathered banner surface */
  .banner {
    position: absolute;
    background:
      repeating-linear-gradient(180deg, rgba(0,0,0,0) 0 13px, rgba(120,95,20,0.10) 13px 14px, rgba(0,0,0,0) 14px 27px),
      linear-gradient(180deg, var(--banner-yellow-light) 0%, var(--banner-yellow) 55%, var(--banner-yellow-deep) 82%, var(--banner-grass) 100%);
  }
  .banner::after {
    content: "";
    position: absolute;
    inset: 0;
    background:
      radial-gradient(ellipse 12% 30% at 0% 10%, rgba(29,26,21,0.35), rgba(29,26,21,0) 70%),
      radial-gradient(ellipse 10% 30% at 100% 15%, rgba(29,26,21,0.35), rgba(29,26,21,0) 70%),
      radial-gradient(ellipse 14% 40% at 100% 100%, rgba(29,26,21,0.25), rgba(29,26,21,0) 70%);
  }

  .title-block {
    left: 0;
    top: 484px;
    width: 402px;
    height: 191px;
    clip-path: polygon(0 3%, 20% 1%, 45% 2%, 70% 0, 96% 1%, 97% 12%, 98.5% 30%, 98% 52%, 99.5% 75%, 100% 100%, 0 100%);
    display: flex;
    align-items: center;
    justify-content: center;
  }
  .series-name {
    position: relative;
    z-index: 1;
    font-family: "Staatliches", "Impact", sans-serif;
    font-weight: 400;
    font-size: 54px;
    line-height: 0.92;
    color: var(--ink);
    letter-spacing: 1px;
    display: flex;
    align-items: center;
    gap: 14px;
    margin-top: 6px;
  }
  .series-mark {
    width: 34px;
    height: 34px;
    border-radius: 50%;
    background: var(--ink);
    flex: none;
  }

  .name-bar {
    left: 452px;
    top: 484px;
    width: 694px;
    height: 92px;
    clip-path: polygon(1% 3%, 25% 1%, 55% 2%, 80% 0, 98.6% 2%, 99.3% 30%, 98.9% 60%, 100% 98%, 60% 100%, 30% 99%, 0.4% 100%, 0.8% 60%, 0 30%);
  }
  .origin-bar {
    left: 432px;
    top: 612px;
    width: 662px;
    height: 63px;
    clip-path: polygon(1.2% 4%, 30% 2%, 60% 3%, 98.2% 0, 99% 35%, 98.6% 65%, 100% 100%, 0 100%, 0.6% 55%);
  }
</style>
</head>
<body>
  <div class="lower-third">
    <div class="scene-photo" role="img" aria-label="Two travellers resting on a rocky lakeshore beside a birch bark canoe among tall reeds"></div>

    <div class="banner title-block">
      <div class="series-name">
        <span class="series-mark"></span>
        <span>Roamers of<br>the Ridge</span>
      </div>
    </div>

    <div class="banner name-bar"></div>
    <div class="banner origin-bar"></div>
  </div>
</body>
</html>
```